Healthcare Technology Company Business Card Design

Hi,

We require a new business card design thats catchy and professional.
Our target audience is healthcare professionals. See supplied artwork for our logo.

If you think its achievable please try add the tag line, not necessary however.
"Developing technologies to improve patient care and release operation benefits"

We'll require the following information on the card. No need to have the subject titles but i've referenced them for your convenience.

Personal Details
Paul Dwyer
Position: Director
Phone Number - 03 9472 5836
Mobile Number - 0438 275 904
Email: firstname.lastname@mediqbay.com.au

Company Details
Suite 31, 286 Keldon Street
Harwick Bay, Kelston
Fax: 03 8241 3975
mediqbay.com.au

Prefer a thinner design than the normal stock standard business card dimensions.
Please ensure there is adequate bleed.

Target Market(s)

Healthcare Professionals

Industry/Entity Type

Healthcare

Font styles to use
Sans Serif

Requirements
Must have
• Clean, Sharp Looks
Should not have
• Any healthcare symbols

```html
<!DOCTYPE html>
<html lang="en">
<head>
<meta charset="utf-8">
<title>MediQbay Business Card</title>
<link href="https://fonts.googleapis.com/css2?family=Tinos:wght@400;700&display=swap" rel="stylesheet">
<style>
  :root {
    --navy: #2c3e63;
    --navy-dark: #1f2d47;
    --orange: #f08a1c;
    --card: #ffffff;
    --ink: #1d2a44;
    --backdrop-start: #050505;
    --backdrop-end: #4a4a4a;
  }
  * { margin: 0; padding: 0; box-sizing: border-box; }
  html, body { width: 1200px; height: 900px; overflow: hidden; }
  body {
    background: linear-gradient(90deg, var(--backdrop-start) 0%, #1a1a1a 45%, var(--backdrop-end) 100%);
    font-family: "Tinos", "Times New Roman", serif;
    position: relative;
  }
  .card {
    position: absolute;
    left: 288px;
    width: 622px;
    height: 352px;
    background: var(--card);
    overflow: hidden;
  }
  .card--front { top: 62px; }
  .card--back { top: 487px; height: 350px; }
  .abs { position: absolute; }

  /* front */
  .brand-mark { width: 22px; height: 22px; background: var(--orange); }
  .brand-name { color: var(--navy); font-weight: 700; white-space: nowrap; line-height: 1; }
  .front-mark { left: 156px; top: 134px; }
  .front-name { left: 192px; top: 118px; font-size: 54px; }
  .front-rule { left: 168px; top: 180px; width: 380px; height: 2px; background: var(--navy); }
  .tagline {
    left: 172px; top: 190px; font-size: 15px; color: var(--navy);
    letter-spacing: -0.3px; white-space: nowrap; transform: scaleX(0.86); transform-origin: left;
  }
  .front-globe { left: 308px; top: 280px; }
  .front-web-rule { left: 192px; top: 298px; width: 248px; height: 2px; background: var(--navy); }
  .front-web { left: 0; width: 632px; text-align: center; top: 304px; font-size: 19px; color: var(--ink); }

  /* back */
  .label-box {
    background: var(--navy-dark);
    color: var(--orange);
    font-size: 28px;
    line-height: 1;
    display: flex; align-items: center; justify-content: center;
    box-shadow: 0 0 5px 2px rgba(31,45,71,0.55);
  }
  .name-box { left: 27px; top: 42px; width: 194px; height: 40px; }
  .company-box { left: 388px; top: 172px; width: 208px; height: 42px; }
  .role { left: 52px; top: 88px; font-size: 25px; color: var(--navy); }
  .back-mark { left: 402px; top: 70px; width: 18px; height: 18px; }
  .back-name { left: 428px; top: 65px; font-size: 30px; }
  .vrule { width: 2px; background: var(--navy-dark); }
  .vrule--personal { left: 34px; top: 119px; height: 96px; }
  .vrule--company { left: 359px; top: 218px; height: 111px; }
  .contact { display: flex; align-items: center; gap: 8px; color: var(--ink); white-space: nowrap; }
  .contact svg { flex: none; }
  .contact--lg { font-size: 21px; }
  .contact--sm { font-size: 17px; }
  .contact--email { transform: scaleX(0.92); transform-origin: left; }
  .address { font-size: 20px; line-height: 26px; letter-spacing: -0.4px; transform: scaleX(0.94); transform-origin: left; }
  .address-block { left: 369px; top: 222px; display: flex; align-items: flex-start; gap: 6px; }
  .address-block svg { margin-top: 12px; }
</style>
</head>
<body>

<section class="card card--front">
  <div class="abs brand-mark front-mark"></div>
  <div class="abs brand-name front-name">MediQbay</div>
  <div class="abs front-rule"></div>
  <p class="abs tagline">Building smart systems to support clinical teams &amp; streamline daily practice.</p>
  <svg class="abs front-globe" width="24" height="20" viewBox="0 0 24 20" aria-hidden="true">
    <circle cx="9" cy="9" r="7" fill="none" stroke="#1d2a44" stroke-width="1.5"/>
    <path d="M2 9h14M9 2c-3 4-3 10 0 14M9 2c3 4 3 10 0 14" fill="none" stroke="#1d2a44" stroke-width="1.2"/>
    <circle cx="16" cy="12" r="3" fill="#fff" stroke="#1d2a44" stroke-width="1.5"/>
    <path d="M18 14l4 4" stroke="#1d2a44" stroke-width="2"/>
  </svg>
  <div class="abs front-web-rule"></div>
  <p class="abs front-web">www.mediqbay.com.au</p>
</section>

<section class="card card--back">
  <div class="abs label-box name-box">Paul Dwyer</div>
  <p class="abs role">Director</p>

  <div class="abs brand-mark back-mark"></div>
  <div class="abs brand-name back-name">MediQbay</div>

  <div class="abs vrule vrule--personal"></div>
  <p class="abs contact contact--lg" style="left:46px; top:125px;">
    <svg width="14" height="14" viewBox="0 0 14 14" aria-hidden="true">
      <rect width="14" height="14" rx="2" fill="#1d2a44"/>
      <path d="M4 3c1 0 1.5 2 1 2.5l-.6.6c.6 1.4 1.6 2.4 3 3l.6-.6c.5-.5 2.5 0 2.5 1 0 1-1 1.5-2 1.3C6 10.2 3.8 8 3.2 5 3 4 3.3 3 4 3z" fill="#fff"/>
    </svg>
    03 9472 5836
  </p>
  <p class="abs contact contact--lg" style="left:46px; top:154px;">
    <svg width="14" height="16" viewBox="0 0 14 16" aria-hidden="true">
      <rect x="3" y="1" width="8" height="14" rx="1.5" fill="none" stroke="#1d2a44" stroke-width="1.5"/>
      <path d="M6 12.5h2" stroke="#1d2a44" stroke-width="1.2"/>
    </svg>
    0438 275 904
  </p>
  <p class="abs contact contact--sm contact--email" style="left:46px; top:187px;">
    <svg width="16" height="12" viewBox="0 0 16 12" aria-hidden="true">
      <rect x="1" y="1" width="14" height="10" fill="none" stroke="#1d2a44" stroke-width="1.2"/>
      <path d="M1 1l7 6 7-6" fill="none" stroke="#1d2a44" stroke-width="1.2"/>
    </svg>
    paul.dwyer@mediqbay.com.au
  </p>

  <div class="abs label-box company-box">MediQbay</div>
  <div class="abs vrule vrule--company"></div>

  <div class="abs address-block">
    <svg width="22" height="14" viewBox="0 0 22 14" aria-hidden="true">
      <path d="M2 8l2-5h10l3 5h3v3H2z" fill="#1d2a44"/>
      <circle cx="6" cy="12" r="2" fill="#1d2a44"/>
      <circle cx="16" cy="12" r="2" fill="#1d2a44"/>
    </svg>
    <p class="contact address">Suite 31, 286 Keldon Street<br>Harwick Bay, Kelston.</p>
  </div>
  <p class="abs contact contact--lg" style="left:373px; top:276px;">
    <svg width="16" height="16" viewBox="0 0 16 16" aria-hidden="true">
      <rect x="3" y="1" width="10" height="14" fill="none" stroke="#1d2a44" stroke-width="1.3"/>
      <path d="M5 5h6M5 8h6M5 11h6" stroke="#1d2a44" stroke-width="1"/>
    </svg>
    03 8241 3975
  </p>
  <p class="abs contact contact--sm" style="left:373px; top:304px;">
    <svg width="16" height="16" viewBox="0 0 24 20" aria-hidden="true">
      <circle cx="9" cy="9" r="7" fill="none" stroke="#1d2a44" stroke-width="1.5"/>
      <path d="M2 9h14M9 2c-3 4-3 10 0 14M9 2c3 4 3 10 0 14" fill="none" stroke="#1d2a44" stroke-width="1.2"/>
      <circle cx="16" cy="12" r="3" fill="#fff" stroke="#1d2a44" stroke-width="1.5"/>
      <path d="M18 14l4 4" stroke="#1d2a44" stroke-width="2"/>
    </svg>
    www.mediqbay.com.au
  </p>
</section>

</body>
</html>
```